Voyage Wellcare Hub Business Cards

We need business cards for our new start-up online travel health clinic. Visit our website voyagewellcarehub.ca for branding and more info.

Target Market(s)

Travellers

Industry/Entity Type

Business

Contact Information for Business Card

Maya Koslowski
maya@voyagewellcarehub.ca
+1 555 283 6194
voyagewellcarehub.ca

Font styles to use
Sans Serif

Colors
f68d4d

```html
<!DOCTYPE html>
<html lang="en">
<head>
<meta charset="utf-8">
<title>Voyage Wellcare Hub Business Cards</title>
<link href="https://fonts.googleapis.com/css2?family=Roboto:wght@300;400;500;700&display=swap" rel="stylesheet">
<style>
  :root {
    --orange: #f68d4d;
    --orange-light: #f6a86f;
    --grey-band: #bdbdbd;
    --grey-soft: #d6d6d6;
    --grey-text: #8a8a8a;
    --white: #ffffff;
    --paper: #fbfbfb;
    --stage: #e9e6e2;
  }
  * { margin: 0; padding: 0; box-sizing: border-box; }
  html, body { width: 1200px; height: 886px; overflow: hidden; }
  body {
    background: var(--stage);
    font-family: "Roboto", sans-serif;
    position: relative;
  }
  .card {
    position: absolute;
    top: 158px;
    width: 330px;
    height: 570px;
    border-radius: 22px;
    overflow: hidden;
    box-shadow: 0 6px 18px rgba(0,0,0,0.18);
  }
  .card--front {
    left: 225px;
    background: linear-gradient(180deg, var(--orange) 0%, var(--orange-light) 60%);
  }
  .card--back {
    left: 645px;
    background: var(--paper);
  }
  .contact {
    position: absolute;
    top: 58px;
    left: 0;
    right: 0;
    text-align: center;
    color: var(--white);
    z-index: 1;
  }
  .contact__icon { display: block; margin: 0 auto 4px; }
  .contact__name {
    font-weight: 500;
    font-size: 22px;
    letter-spacing: 0.5px;
    text-transform: uppercase;
    margin-bottom: 20px;
  }
  .contact__line {
    font-size: 13.5px;
    font-weight: 400;
    margin-bottom: 7px;
  }
  .front-art {
    position: absolute;
    left: 0;
    bottom: 0;
    width: 330px;
    height: 300px;
    display: block;
  }
  .brand {
    position: absolute;
    top: 240px;
    left: 0;
    right: 0;
    text-align: center;
  }
  .brand__name {
    font-size: 26px;
    font-weight: 300;
    color: var(--orange);
    display: inline-flex;
    align-items: center;
    gap: 8px;
  }
  .brand__dot {
    width: 10px; height: 10px; border-radius: 50%;
    background: var(--orange);
  }
  .brand__tagline {
    margin-top: 4px;
    font-size: 11px;
    color: var(--grey-text);
    letter-spacing: 0.6px;
  }
  .web-band {
    position: absolute;
    left: 0;
    right: 0;
    bottom: 64px;
    height: 34px;
    background: var(--grey-band);
    color: var(--white);
    font-size: 12.5px;
    letter-spacing: 3.5px;
    display: flex;
    align-items: center;
    justify-content: center;
  }
</style>
</head>
<body>

  <section class="card card--front" aria-label="Business card front">
    <div class="contact">
      <svg class="contact__icon" width="14" height="14" viewBox="0 0 14 14" aria-hidden="true">
        <circle cx="7" cy="4" r="3.2" fill="#fff"/>
        <path d="M1 14 C1 9 13 9 13 14 Z" fill="#fff"/>
      </svg>
      <div class="contact__name">Maya Koslowski</div>

      <svg class="contact__icon" width="12" height="12" viewBox="0 0 12 12" aria-hidden="true">
        <path d="M2.5 1 L4.5 1 L5.3 3.5 L4 4.6 C4.8 6.3 5.8 7.3 7.4 8 L8.5 6.7 L11 7.5 L11 9.5 C11 10.3 10.3 11 9.5 11 C5 11 1 7 1 2.5 C1 1.7 1.7 1 2.5 1 Z" fill="#fff"/>
      </svg>
      <div class="contact__line">+1 555 283 6194</div>

      <svg class="contact__icon" width="13" height="10" viewBox="0 0 13 10" aria-hidden="true">
        <rect x="0.5" y="0.5" width="12" height="9" rx="1" fill="#fff"/>
        <path d="M1 1 L6.5 5.5 L12 1" stroke="#f68d4d" stroke-width="1" fill="none"/>
      </svg>
      <div class="contact__line">maya@voyagewellcarehub.ca</div>

      <svg class="contact__icon" width="13" height="13" viewBox="0 0 13 13" aria-hidden="true">
        <circle cx="6.5" cy="6.5" r="6" fill="#fff"/>
        <path d="M0.5 6.5 H12.5 M6.5 0.5 C3.5 4 3.5 9 6.5 12.5 M6.5 0.5 C9.5 4 9.5 9 6.5 12.5" stroke="#f68d4d" stroke-width="0.8" fill="none"/>
      </svg>
      <div class="contact__line">www.voyagewellcarehub.ca</div>
    </div>

    <svg class="front-art" viewBox="0 0 330 300" role="img" aria-label="Large white airplane silhouette flying across a grey band">
      <defs>
        <linearGradient id="planeArea" x1="0" y1="0" x2="0" y2="1">
          <stop offset="0" stop-color="#f7f4f1"/>
          <stop offset="0.55" stop-color="#e2e2e2"/>
          <stop offset="1" stop-color="#c4c4c4"/>
        </linearGradient>
      </defs>
      <polygon points="0,90 330,30 330,300 0,300" fill="url(#planeArea)"/>
    </svg>
  </section>

  <section class="card card--back" aria-label="Business card back">
    <div class="brand">
      <div class="brand__name"><span class="brand__dot"></span>Voyage Wellcare Hub</div>
      <div class="brand__tagline">Online Travel Health Experts</div>
    </div>
    <div class="web-band">www.voyagewellcarehub.ca</div>
  </section>

</body>
</html>
```